Flyer design for VIP membership

We need an A4 flyer design for our automotive workshop explaining and advertising to our customers about our VIP membership.

We are a modern and new workshop in New Zealand. I have attached our business card and another design for you to view. Along with company logo. Our colours are black, white and red.

Design needs to stand out and be easy to read.

Design must include the following wording:
___________________________________________________________________--

BLUESTONE TOTAL AUTOMOTIVE
VIP
FLEET VEHICLE SERVICING AND MAINTENANCE
Tradie?
Business owner?
Own 3 or more vehicles?
Become an Bluestone VIP member and receive:
• 10% off Vehicle Servicing and Mechanical Repairs
• 10% off Tyres
• Free basic vehicle exterior wash with every job
• Free puncture repairs
• Vehicle Delivery and Pick up
• Vehicle WOF, Service and Wheel Alignment reminders
• Given quick and first choice on all bookings and appointments
• Organise a tow truck to workshop for local break downs

If you’ve got a fleet of vehicles for your business, Bluestone can make it easy for you to stay on top of your servicing and maintenance schedules. We offer peace of mind motoring that ensures your vehicles are safe and reliable at cost effective prices.
Bluestone is your one stop automotive shop. We aim to make your automotive servicing and repairs as easy and painless as possible. We pride ourselves on excellent customer service and quality workmanship in a professional manner at competitive rates, using the latest technology and equipment.

Our services include:
• Vehicle Servicing
• All Mechanical Repairs
• Brakes, steering and suspension
• Transmission and cooling system servicing
• Warrant of fitness inspections
• Safety checks and pre-purchase inspections
• Tyres and wheel alignments
• Puncture repairs
• Mag wheels
• Vehicle Lowering and lift kits
• Automotive diagnostics
• Trailer repairs, maintenance and parts
• Automotive parts and supplies
• 4WD accessories
• Batteries
• And more
Contact us today to enquire about becoming an Bluestone VIP member.
Phone: 07 452 3917
Email: office@bluestoneautoworks.example.nz
Website: www.bluestoneautoworks.example.nz

```html
<!DOCTYPE html>
<html lang="en">
<head>
<meta charset="utf-8">
<title>Bluestone Total Automotive – VIP Fleet Membership</title>
<link rel="stylesheet" href="https://fonts.googleapis.com/css2?family=Fira+Sans+Condensed:ital,wght@1,600&family=Source+Sans+3:ital,wght@0,400;0,600;0,700;1,600;1,700&display=swap">
<style>
  :root {
    --red: #e8202a;
    --red-dark: #9e0b12;
    --black: #0d0d0d;
    --ink: #111111;
    --grey: #8a8a8a;
    --white: #ffffff;
    --silver: #cfcfcf;
  }
  * { margin: 0; padding: 0; box-sizing: border-box; }
  html, body { width: 848px; height: 1200px; overflow: hidden; background: var(--white); }
  .flyer {
    position: relative; width: 848px; height: 1200px; overflow: hidden;
    font-family: "Source Sans 3", sans-serif; color: var(--ink); background: var(--white);
  }
  .backdrop { position: absolute; inset: 0; }
  .abs { position: absolute; }

  .brand { left: 383px; top: 50px; width: 432px; color: var(--red); font-weight: 700; text-align: center; }
  .brand-name { font-size: 58px; line-height: 1; letter-spacing: 4px; }
  .brand-sub { font-size: 18px; letter-spacing: 8px; margin-top: 6px; }

  .headline { left: 25px; top: 100px; color: var(--white); font-weight: 400; line-height: 43px; }
  .headline span { display: block; font-size: 44px; }
  .headline .big { font-size: 56px; line-height: 50px; }

  .questions {
    right: 553px; top: 306px; text-align: right;
    font-family: "Fira Sans Condensed", sans-serif; font-style: italic; font-weight: 600;
    color: var(--white); font-size: 25px; line-height: 32px;
  }
  .questions span { display: inline-block; border-bottom: 2px solid var(--white); line-height: 30px; }

  .become {
    right: 546px; top: 440px; text-align: right; color: var(--white);
    font-size: 40px; line-height: 42px; font-weight: 400;
  }

  .badge {
    left: 310px; top: 219px; width: 262px; height: 262px; border-radius: 50%;
    background: radial-gradient(circle at 50% 50%, #111 0 42%, #d6d6d6 43% 70%, #a8a8a8 100%);
  }

  .benefits {
    left: 13px; width: 340px; top: 700px; text-align: center; list-style: none;
    font-style: italic; font-weight: 700; font-size: 19px; line-height: 24px;
  }
  .benefits li { margin-bottom: 6px; }
  .benefits li.alt { color: var(--red); }

  .intro {
    left: 578px; top: 188px; width: 250px; color: var(--white);
    font-size: 14px; line-height: 20px; text-align: justify;
  }

  .services-title { left: 452px; top: 625px; font-size: 31px; color: var(--white); font-weight: 400; }
  .services-title em { font-style: normal; color: var(--red); }
  .services { left: 400px; top: 678px; list-style: none; color: var(--white); font-size: 19px; }
  .services li { position: relative; height: 25.2px; line-height: 25px; padding-left: 55px; }
  .services li::before {
    content: "›"; position: absolute; left: 0; top: 3px; width: 19px; height: 19px; border-radius: 50%;
    background: var(--red); color: var(--white); font-weight: 700; font-size: 16px; line-height: 17px; text-align: center;
  }

  .cta { left: 27px; top: 1118px; color: var(--white); font-weight: 600; font-size: 14px; line-height: 24px; }
  .call { left: 389px; top: 1117px; color: #ffe3e4; font-size: 20px; line-height: 26px; font-weight: 600; }
  .web-icon { left: 521px; top: 1133px; width: 22px; height: 22px; }
  .contact { left: 553px; top: 1118px; color: var(--white); font-size: 16.5px; line-height: 26px; }
</style>
</head>
<body>
<main class="flyer">
  <svg class="backdrop" width="848" height="1200" viewBox="0 0 848 1200" aria-hidden="true">
    <defs>
      <linearGradient id="swoosh" x1="0" y1="0" x2="1" y2="1">
        <stop offset="0" stop-color="#ff2a2a"/>
        <stop offset="0.55" stop-color="#d4121b"/>
        <stop offset="1" stop-color="#7a0a0f"/>
      </linearGradient>
      <linearGradient id="panelGlow" x1="0" y1="0" x2="0" y2="1">
        <stop offset="0" stop-color="#0d0d0d"/>
        <stop offset="0.55" stop-color="#120405"/>
        <stop offset="1" stop-color="#5a070c"/>
      </linearGradient>
    </defs>

    <path d="M0,47 H280 Q300,47 315,62 L470,220 L470,470 L330,610 Q300,640 270,640 H0 Z" fill="var(--black)"/>
    <path d="M0,375 C140,395 300,430 440,470 L330,610 Q300,640 270,640 H0 Z" fill="url(#swoosh)"/>
    <path d="M0,640 H210 L185,675 H0 Z" fill="var(--black)"/>

    <path d="M470,215 L555,148 Q572,134 600,134 H848 V557 H612 Q590,557 572,543 L470,470 Z" fill="var(--red)"/>
    <path d="M470,240 L578,182 Q590,172 606,172 H848 V523 H614 Q596,523 580,511 L470,440 Z" fill="var(--grey)"/>

    <path d="M405,575 H848 V1200 H365 V622 Q365,602 380,592 Z" fill="url(#panelGlow)"/>

    <path d="M285,1113 H848 V1176 H372 Z" fill="var(--red)"/>
    <path d="M0,1087 H250 Q266,1087 280,1098 L372,1176 H0 Z" fill="var(--black)"/>
  </svg>

  <div class="abs brand">
    <div class="brand-name">BLUESTONE</div>
    <div class="brand-sub">TOTAL AUTOMOTIVE</div>
  </div>

  <h1 class="abs headline">
    <span>FLEET VEHICLE</span>
    <span>SERVICING AND</span>
    <span class="big">MAINTENANCE</span>
  </h1>

  <p class="abs questions">
    <span>Tradie?</span><br>
    <span>Business owner?</span><br>
    <span>Own 3 or more vehicles?</span>
  </p>

  <h2 class="abs become">BECOME<br>AN BLUESTONE<br>VIP&nbsp; MEMBER<br>AND&nbsp; RECEIVE:</h2>

  <div class="abs badge" role="img" aria-label="Silver gear-shaped VIP membership badge with a crown and three stars"></div>

  <p class="abs intro">If you’ve got a fleet of vehicles for your business, Bluestone can make it easy for you to stay on top of your servicing and maintenance schedules. We offer peace of mind motoring that ensures your vehicles are safe and reliable at cost effective prices. Bluestone is your one stop automotive shop. We aim to make your automotive servicing and repairs as easy and painless as possible. We pride ourselves on excellent customer service and quality workmanship in a professional manner at competitive rates, using the latest technology and equipment.</p>

  <ul class="abs benefits">
    <li>10% off Vehicle Servicing<br>and Mechanical Repairs</li>
    <li class="alt">10% off Tyres</li>
    <li>Free basic vehicle exterior<br>wash with every job</li>
    <li class="alt">Free puncture repairs</li>
    <li>Vehicle Delivery and Pick up</li>
    <li class="alt">Vehicle WOF, Service and<br>Wheel Alignment reminders</li>
    <li>Given quick and first choice on<br>all bookings and appointments</li>
    <li class="alt">Organise a tow truck to workshop<br>for local break downs</li>
  </ul>

  <h2 class="abs services-title"><em>OUR SERVICES</em> INCLUDE:</h2>
  <ul class="abs services">
    <li>Vehicle Servicing</li>
    <li>All Mechanical Repairs</li>
    <li>Brakes, steering and suspension</li>
    <li>Transmission and cooling system servicing</li>
    <li>Warrant of fitness inspections</li>
    <li>Safety checks and pre-purchase inspections</li>
    <li>Tyres and wheel alignments</li>
    <li>Puncture repairs</li>
    <li>Mag wheels</li>
    <li>Vehicle Lowering and lift kits</li>
    <li>Automotive diagnostics</li>
    <li>Trailer repairs, maintenance and parts</li>
    <li>Automotive parts and supplies</li>
    <li>4WD accessories</li>
    <li>Batteries</li>
    <li>And more</li>
  </ul>

  <p class="abs cta">CONTACT US TODAY TO ENQUIRE ABOUT<br>BECOMING AN BLUESTONE VIP MEMBER.</p>
  <p class="abs call">CALL NOW<br>07 452 3917</p>
  <svg class="abs web-icon" viewBox="0 0 22 22" aria-hidden="true">
    <circle cx="11" cy="11" r="10" fill="var(--white)"/>
    <circle cx="11" cy="11" r="7" fill="none" stroke="var(--red)" stroke-width="1.4"/>
    <ellipse cx="11" cy="11" rx="3" ry="7" fill="none" stroke="var(--red)" stroke-width="1.2"/>
    <line x1="4" y1="11" x2="18" y2="11" stroke="var(--red)" stroke-width="1.2"/>
  </svg>
  <p class="abs contact">office@bluestoneautoworks.example.nz<br>www.bluestoneautoworks.example.nz</p>
</main>
</body>
</html>
```